Car show marketing A5 one sided leaflet/brochure

We are a car enthusiast group that is hosting a performance vehicle trade show & show and shine event. We require a Brochure/leaflet advertising this trade show . Not folded. Just one sided A5 leaflet. We were liking the look of car headlights (but for the car make/model to be non-descript) just that it is an actual car ... Moody ... there will be a DJ playing and arcade racing etc. so that type of 'electronic' fun, motor enthuiast feel. Plus in the background or somewhere on it have the hall in which we are hosting it. I have attached a photo of the hall. The expo is called "Midland Gearworks Fair" being hosted by "Tarnby Motorsport" The catchfrase is "Fueling Roadside Kinship" I have also attached the tarnby motorsport logo. It will be at the "The Calloway Pavilion" Brisbane on 9th March 2024 from 9.30am to 5pm. It will be showcasing automotive businesses. Please have somewhere on the brochure there will be live entertainment and kids entertainment. Catering throughout the event. (Food stalls & cafe). Entry just $25 - kids under 12 free. See website for details. www.tarnbymotorsport.example.au *** I have attached a picture of a idea we had thrown together but obviously we are not in any way able to put together the flyer as we have no experience. We are open for any other design ideas. Thank you!!

Target Market(s)

Car Enthusiasts & families

Industry/Entity Type

Motor

Font styles to use
Serif
Other font styles liked:
• Car racing font such as outrider for example only

Requirements
Must have
• Car feel

```html
<!DOCTYPE html>
<html lang="en">
<head>
<meta charset="utf-8">
<title>Midland Gearworks Fair</title>
<link rel="stylesheet" href="https://fonts.googleapis.com/css2?family=Orbitron:wght@500;700&family=Racing+Sans+One&display=swap">
<style>
  :root {
    --red: #e2332a;
    --ink: #1c1b1b;
    --white: #ffffff;
    --night: #151515;
  }
  * { margin: 0; padding: 0; box-sizing: border-box; }
  html, body { width: 846px; height: 1200px; overflow: hidden; background: var(--night); }
  .leaflet {
    position: relative; width: 846px; height: 1200px; overflow: hidden;
    font-family: "Orbitron", sans-serif; color: var(--white);
  }
  .hero-photo {
    position: absolute; inset: 0;
    background:
      linear-gradient(180deg, rgba(20,20,20,.85) 0%, rgba(20,20,20,0) 14%),
      radial-gradient(ellipse 60% 45% at 22% 52%, #d5431f 0%, #a3301a 45%, rgba(80,30,25,0) 80%),
      radial-gradient(ellipse 40% 50% at 85% 35%, #5b6f86 0%, rgba(60,70,90,0) 75%),
      linear-gradient(160deg, #4a4f57 0%, #2f2f33 55%, #1f1f21 100%);
  }
  .slanted { font-style: oblique 10deg; }
  .event-when {
    position: absolute; left: 0; width: 846px; top: 62px;
    text-align: center; font-weight: 500; font-size: 25px; line-height: 39px;
    letter-spacing: 1.5px;
  }
  .tagline {
    position: absolute; left: 40px; top: 455px; width: 760px; height: 48px;
    background: linear-gradient(90deg, rgba(226,51,42,0) 0%, var(--red) 12%, var(--red) 88%, rgba(226,51,42,0) 100%);
  }
  .tagline span {
    position: absolute; left: 0; right: 0; top: 7px; text-align: center;
    font-family: "Racing Sans One", sans-serif; font-size: 31px; letter-spacing: 1.5px;
  }
  .title-band {
    position: absolute; background: var(--white); color: var(--ink);
    font-family: "Racing Sans One", sans-serif; line-height: 1; white-space: nowrap;
  }
  .title-band--one { left: 0; top: 523px; width: 785px; height: 84px; }
  .title-band--two { left: 200px; top: 607px; width: 646px; height: 76px; }
  .title-band--one .word { position: absolute; left: 150px; top: 4px; font-size: 84px; letter-spacing: 1px; }
  .title-band--two .word { position: absolute; left: 22px; top: 5px; font-size: 70px; }
  .stripes { position: absolute; }
  .stripes--left { left: 0; top: 530px; }
  .stripes--right { left: 650px; top: 628px; }
  .title-box {
    position: absolute; left: 382px; top: 683px; width: 285px; height: 86px;
    background: var(--red); color: var(--ink);
    font-family: "Racing Sans One", sans-serif; font-size: 84px; line-height: 1;
    text-align: center; padding-top: 2px;
  }
  .extras {
    position: absolute; left: 43px; top: 893px;
    font-weight: 500; font-size: 20px; line-height: 29px; letter-spacing: 1px;
    text-transform: uppercase;
  }
  .entry { position: absolute; left: 0; top: 1012px; width: 330px; height: 188px; }
  .entry-text { position: absolute; left: 0; width: 315px; text-align: center; }
  .entry-label { top: 1030px; font-family: "Racing Sans One", sans-serif; font-size: 34px; letter-spacing: 1px; }
  .entry-price { top: 1062px; font-family: "Racing Sans One", sans-serif; font-size: 72px; line-height: 1; }
  .entry-note { top: 1130px; font-weight: 500; font-size: 19px; line-height: 30px; letter-spacing: 1px; }
  .host { position: absolute; right: 46px; top: 1010px; width: 400px; text-align: right; }
  .host-label { font-weight: 500; font-size: 17px; letter-spacing: 2px; margin-right: 30px; }
  .host-marks { display: flex; justify-content: flex-end; align-items: center; gap: 22px; margin-top: 20px; }
  .host-name { font-weight: 700; font-size: 19px; letter-spacing: 1px; color: var(--white); }
  .partner-badge { width: 34px; height: 42px; border: 4px solid var(--red); border-radius: 8px; }
  .more-info { position: absolute; right: 46px; top: 1113px; font-weight: 500; font-size: 17px; letter-spacing: 1.5px; }
  .website { position: absolute; right: 44px; top: 1147px; font-weight: 700; font-size: 20px; letter-spacing: 1px; }
</style>
</head>
<body>
<main class="leaflet">
  <div class="hero-photo" role="img" aria-label="Moody close-up of a red performance car's headlight and front grille beside a painted wall and paved ground"></div>

  <p class="event-when slanted">9TH MARCH 2024 FROM 9.30AM TO 5PM<br>AT "THE CALLOWAY PAVILION" BRISBANE</p>

  <div class="tagline"><span>FUELING ROADSIDE KINSHIP</span></div>

  <svg class="stripes stripes--left" width="58" height="60" aria-hidden="true">
    <rect x="0" y="0" width="58" height="10" fill="var(--ink)"/>
    <rect x="0" y="22" width="52" height="10" fill="var(--ink)"/>
    <rect x="0" y="44" width="48" height="10" fill="var(--ink)"/>
  </svg>
  <div class="title-band title-band--one"><span class="word">MIDLAND</span></div>
  <div class="title-band title-band--two"><span class="word">GEARWORKS</span></div>
  <svg class="stripes stripes--right" width="196" height="40" aria-hidden="true">
    <rect x="0" y="0" width="196" height="7" fill="var(--ink)"/>
    <rect x="0" y="15" width="196" height="7" fill="var(--ink)"/>
    <rect x="0" y="30" width="196" height="7" fill="var(--ink)"/>
  </svg>
  <div class="title-box">FAIR</div>

  <p class="extras slanted">Live entertainment,<br>kids activities and<br>food will be available</p>

  <svg class="entry" viewBox="0 0 330 188" aria-hidden="true">
    <polygon points="0,0 328,0 296,188 0,188" fill="var(--red)"/>
  </svg>
  <p class="entry-text entry-label">ENTRY</p>
  <p class="entry-text entry-price">$25</p>
  <p class="entry-text entry-note slanted">FREE FOR KIDS<br>UNDER 12</p>

  <div class="host">
    <p class="host-label slanted">HOSTED BY</p>
    <div class="host-marks">
      <span class="host-name">TARNBY MOTORSPORT</span>
      <span class="partner-badge" aria-label="Partner badge"></span>
    </div>
  </div>
  <p class="more-info slanted">FOR MORE INFO VISIT</p>
  <p class="website slanted">WWW.TARNBYMOTORSPORT.EXAMPLE.AU</p>
</main>
</body>
</html>
```